Corporate Identity Design Project

Teslin Varrow Design is a small boutique event planning and floral design company, based in Northern Alberta. I require the creation of some corporate identity pieces. I want a minimalistic design.
Website www.teslinvarrow.example

Pieces should include
1. Business Card
Should include the company logo, name, email address, address, phone number. These will be professional printed.
These are three cards that I like:
http://cardsamplegallery.example/wp-content/uploads/2010/02/Odile_Vantreck_Roomworks_by_Pepperleaf_studio_Media.jpg
http://neatcardshowcase.example/wp-content/uploads/2011/06/Quiet-Studio-Minimalist-Business-Cards_11.jpg
http://graphicfeedhub.example/wp-content/uploads/2012/03/16.minimalist-business-cards.jpg
I like letterpress, but I am open to other options.

2. Letterhead
will be professionally printed

3. Envelope

4. Fax Sheet
will be printed on home printer

5. Pocket Presentation
Like -http://wrenfieldgardens.example/img/design_step_proposal@2x.jpg

6. Invoice
Like - http://samplehost.example/quillmarsh/2011/02/falcon-athletics-4-letterhead-combined.png?w=529

7. Proposal
Like something like this – this will not be printed, but rather emailed to clients
Like http://files7.imagedepot.example/getfile/files.imagedepot.example/trelvo-studio/nkuBfi2LVj7ENiUb5D16wqAHQHqNNT5vut7mukSTmisfoGHYXGEv9haEQOPL/Picture-52.png.scaled.500.jpg

8. Contract
Like http://www.brightkeyadvertising.example/images/sample-contract.jpg

9. Business Brochure – I have removed this piece from the project and will most likely post it as another project at a later date.

If you think that this is a project of interest to you, but feel that it is “too much” work for the price, please let me know how you would re-package it – I am open to suggestions.

Target Market(s)

Young women

Industry/Entity Type

Boutique

Requirements
Should not have
• I do not want it to look "frilly"

```html
<!DOCTYPE html>
<html lang="en">
<head>
<meta charset="utf-8">
<title>Teslin Varrow Design – Pocket Presentation Folder</title>
<link rel="stylesheet" href="https://fonts.googleapis.com/css2?family=Josefin+Sans:wght@400&family=Lato:wght@400;700&display=swap">
<style>
  :root {
    --backdrop: #eceded;
    --folder-brown: #725e55;
    --folder-brown-deep: #64524a;
    --art-tone: #8f7c73;
    --art-light: #a4938b;
    --paper: #ffffff;
    --ink: #2f2a28;
    --rule: #b9b3b0;
    --slit: #4f3f39;
    --logo-white: #f6f2ef;
  }
  * { box-sizing: border-box; margin: 0; padding: 0; }
  html, body {
    width: 1200px;
    height: 910px;
    overflow: hidden;
    background: var(--backdrop);
  }
  .spread {
    position: relative;
    width: 1200px;
    height: 910px;
  }

  /* Front cover */
  .cover {
    position: absolute;
    left: 150px;
    top: 100px;
    width: 430px;
    height: 710px;
    background: var(--folder-brown);
  }
  .cover__wordmark {
    position: absolute;
    right: 40px;
    top: 52px;
    font-family: "Josefin Sans", sans-serif;
    font-weight: 400;
    font-size: 30px;
    line-height: 1.05;
    letter-spacing: 2px;
    text-transform: uppercase;
    color: var(--logo-white);
  }
  .cover__art-area {
    position: absolute;
    left: 40px;
    top: 390px;
    width: 190px;
    height: 290px;
    background: linear-gradient(160deg, var(--art-light) 0%, var(--art-tone) 100%);
  }

  /* Inside right panel */
  .inside {
    position: absolute;
    left: 620px;
    top: 100px;
    width: 430px;
    height: 710px;
    background: var(--folder-brown-deep);
  }
  .sheet {
    position: absolute;
    left: 24px;
    top: 24px;
    width: 382px;
    height: 560px;
    background: var(--paper);
    padding: 34px 34px 0;
    font-family: "Lato", sans-serif;
    color: var(--ink);
    overflow: hidden;
  }
  .sheet__title {
    font-weight: 700;
    font-size: 20px;
    margin-bottom: 18px;
  }
  .sheet__table {
    width: 100%;
    border-collapse: collapse;
    margin-bottom: 22px;
  }
  .sheet__table td {
    height: 26px;
    border: 1px solid var(--rule);
  }
  .sheet__clause {
    font-size: 11px;
    line-height: 1.5;
    margin-bottom: 10px;
  }

  .pocket {
    position: absolute;
    left: 0;
    bottom: 0;
    width: 430px;
    height: 210px;
    background: var(--folder-brown);
    border-top: 1px solid #5c4a43;
  }
  .pocket__slits {
    position: absolute;
    left: 60px;
    top: 20px;
  }
  .business-card {
    position: absolute;
    left: 70px;
    top: 30px;
    width: 160px;
    height: 96px;
    background: var(--paper);
    padding: 12px;
    font-family: "Lato", sans-serif;
    color: var(--ink);
    font-size: 7.5px;
    line-height: 1.45;
    white-space: nowrap;
  }
  .business-card__name {
    font-weight: 700;
    font-size: 8.5px;
    margin-bottom: 6px;
  }
</style>
</head>
<body>
<main class="spread">

  <section class="cover" aria-label="Folder front cover">
    <div class="cover__wordmark">Teslin<br>Varrow<br>Design</div>
    <div class="cover__art-area" role="img" aria-label="Area for the cover's loose line-drawn floral ornament in cream and taupe"></div>
  </section>

  <section class="inside" aria-label="Folder inside panel with pocket">
    <article class="sheet">
      <h1 class="sheet__title">Terms &amp; Fees</h1>
      <table class="sheet__table">
        <tr><td></td><td></td></tr>
        <tr><td></td><td></td></tr>
        <tr><td></td><td></td></tr>
        <tr><td></td><td></td></tr>
      </table>
      <p class="sheet__clause">Thank you for choosing us. By signing, both parties agree to these terms.</p>
      <p class="sheet__clause">Floral designs are perishable; we hold no liability after delivery.</p>
      <p class="sheet__clause">Changes require seven days of notice.</p>
      <p class="sheet__clause">Room setup time is limited to the hours booked.</p>
      <p class="sheet__clause">Final payment is due five days before the event.</p>
      <p class="sheet__clause">The deposit is non-refundable once orders are placed.</p>
    </article>

    <div class="pocket">
      <div class="business-card">
        <p class="business-card__name">Teslin Varrow Design Ltd</p>
        <p>hello@teslinvarrow.example</p>
        <p>000.555.0148</p>
        <p>Suite 200 – 14 Alder Row</p>
        <p>Larkspur Falls, AB X0X 0X0</p>
      </div>
      <svg class="pocket__slits" width="190" height="120" viewBox="0 0 190 120" aria-hidden="true">
        <line x1="0" y1="22" x2="22" y2="0" stroke="var(--slit)" stroke-width="1.5"/>
        <line x1="160" y1="0" x2="182" y2="22" stroke="var(--slit)" stroke-width="1.5"/>
        <line x1="0" y1="98" x2="22" y2="120" stroke="var(--slit)" stroke-width="1.5"/>
        <line x1="160" y1="120" x2="182" y2="98" stroke="var(--slit)" stroke-width="1.5"/>
      </svg>
    </div>
  </section>

</main>
</body>
</html>
```